R J Penn Accounting & SMSF Auditing needs a Web Site Design

I need some examples of what a web design can look like for my business.
The business name is above and I have already registered a domain name of www.penn-smsf.com.au
I have attached my current letterhead and business cards and would like to maintain these colours basically Red on White with some black

Industry/Entity Type

Business

```html
<!DOCTYPE html>
<html lang="en">
<head>
<meta charset="utf-8">
<title>R J Penn Accounting &amp; SMSF Auditing</title>
<link rel="stylesheet" href="https://fonts.googleapis.com/css2?family=Comfortaa:wght@500&family=Open+Sans:wght@400;600&family=Oswald:wght@400&family=Permanent+Marker&display=swap">
<style>
:root{
  --red:#c8102e;
  --red-dark:#a80d26;
  --ink:#3a3a3a;
  --text:#8a8a8a;
  --muted:#a5a5a5;
  --line:#e4e4e4;
  --panel:#f5f5f5;
  --white:#ffffff;
}
*{margin:0;padding:0;box-sizing:border-box}
html,body{width:1036px;height:1200px;overflow:hidden;background:var(--white)}
body{position:relative;font-family:"Open Sans",Arial,sans-serif;color:var(--ink)}
.abs{position:absolute}

.brand{left:150px;top:22px;white-space:nowrap}
.brand-name{font-family:Arial,Helvetica,sans-serif;font-weight:700;font-size:27px;color:var(--red);letter-spacing:.5px}
.brand-tag{font-family:"Comfortaa",sans-serif;font-size:24px;color:var(--ink);margin-left:8px}
.brand-sub{left:302px;top:62px;font-family:"Comfortaa",sans-serif;font-size:17px;color:var(--ink)}
.head-social{left:795px;top:44px;display:flex;gap:4px}
.head-social span{width:21px;height:21px;background:#cfcfcf}

.nav{left:148px;top:103px;width:741px;height:47px;border:1px solid var(--line);background:linear-gradient(#fafafa,#f0f0f0);display:flex}
.nav a{display:flex;align-items:center;justify-content:center;font-size:12px;color:#666;text-decoration:none;text-transform:uppercase;border-right:1px dashed #d6d6d6;height:100%}
.nav a.active{background:var(--red);color:var(--white);font-weight:600;border:none}
.nav a:last-child{border-right:none}

.slider{left:148px;top:163px;width:741px;height:326px;background:linear-gradient(100deg,#3b3d45 0%,#6d6e73 30%,#d9d5d0 55%,#e9e9ec 75%,#b7bcc4 100%);border-radius:3px}
.caption{left:626px;top:251px;width:263px;height:141px;background:rgba(90,90,90,.82);padding:12px 20px}
.caption h1{font-family:"Oswald",sans-serif;font-weight:400;font-size:33px;color:var(--white);line-height:1.1;white-space:nowrap;letter-spacing:-.5px}
.caption p{font-size:10px;line-height:16px;color:#f2f2f2;margin-top:10px}
.dots{display:flex;gap:4px;margin-top:10px}
.dots span{width:10px;height:10px;border-radius:50%;background:#e8e8e8}
.dots span.on{background:var(--red)}

.section-title{font-size:18px;color:#555;font-weight:400}
.section-title em{font-style:normal;color:var(--red)}
.welcome-title{left:148px;top:516px}
.welcome-photo{left:149px;top:554px;width:172px;height:172px;background:linear-gradient(120deg,#f3ece6,#d9cbbd 45%,#e6e9ee)}
.welcome-body{left:340px;top:550px;width:297px}
.welcome-body h3{font-size:14px;font-weight:400;color:#666;margin-bottom:12px}
.welcome-body p{font-size:9.6px;line-height:17px;color:var(--muted);text-align:justify;margin-bottom:16px}

.testi-title{left:655px;top:516px}
.testi-dots{left:851px;top:524px;display:flex;gap:3px}
.testi-dots span{width:6px;height:6px;border-radius:50%;background:#ddd}
.testi-dots span.on{background:#f07a1a}
.quote{left:655px;top:552px;width:233px;height:150px;background:var(--panel);padding:32px 16px 0 20px}
.quote p{font-size:9.6px;line-height:18.5px;color:var(--text)}
.qmark{font-family:Georgia,serif;font-size:26px;color:#bbb;position:absolute}
.quote-author{left:811px;top:714px;font-size:11px;color:#555}

.service-photo{top:762px;width:234px;height:130px}
.s1{left:149px;background:linear-gradient(110deg,#4a5568,#9aa4b4 50%,#e2d6c8)}
.s2{left:402px;background:linear-gradient(110deg,#2c3140,#cfd8e4 50%,#f1f3f6)}
.service{top:910px;width:236px}
.service h3{font-size:14px;font-weight:400;color:#555;margin-bottom:12px}
.service p{font-size:9.6px;line-height:18px;color:var(--muted);text-align:justify}

.news-head{left:655px;top:762px;width:234px;height:33px;background:var(--red);color:var(--white);font-size:14px;padding:8px 14px}
.news-arrows{position:absolute;right:16px;top:5px;display:flex;gap:18px;font-size:14px}
.news-item{left:655px;width:234px;height:98px;display:flex;gap:14px}
.news-item .thumb{width:74px;height:80px;flex:none}
.news-item h4{font-size:12.5px;font-weight:400;color:#666;line-height:18px;margin-bottom:10px}
.news-item p{font-size:9.6px;line-height:16.5px;color:var(--muted);text-align:justify}
.n1{top:812px}
.n1 .thumb{background:linear-gradient(120deg,#5c7fb5,#dfe6ef)}
.n2{top:925px}
.n2 .thumb{background:linear-gradient(120deg,#e8eaee,#6a7a90)}
.news-sep{left:655px;top:909px;width:234px;height:1px;background:var(--line)}

.footer{left:148px;top:1046px;width:741px;height:121px;border:1px solid #ececec;background:#fcfcfc}
.fcol{top:1062px}
.fcol h4{font-size:15px;font-weight:400;color:#555;margin-bottom:10px}
.fcol li{list-style:none;font-size:10px;color:#777;line-height:22px}
.fcol li::before{content:"›";margin-right:8px;color:#999}
.call-icons{left:515px;top:1064px}
.call{left:586px;top:1064px}
.call .label{font-family:"Permanent Marker",cursive;font-size:17px;color:#333}
.call .phone{font-size:20px;color:var(--red);margin-top:2px}
.call .mail{font-size:12px;color:var(--red);margin-top:5px}
.badge{left:782px;top:1060px;width:40px;height:40px;border-radius:50%;border:2px solid #555}
.copy{left:754px;top:1105px;font-size:9.5px;color:#777;white-space:nowrap}
.foot-social{left:767px;top:1129px;display:flex;gap:5px}
.foot-social span{width:22px;height:22px;border-radius:50%}
</style>
</head>
<body>

<header>
  <div class="abs brand"><span class="brand-name">R J Penn</span><span class="brand-tag">Accounting &amp; SMSF Auditing</span></div>
  <div class="abs brand-sub">Penrose Penn Pty Ltd T/A</div>
  <div class="abs head-social" aria-label="Social links"><span></span><span></span><span></span><span></span></div>
</header>

<nav class="abs nav">
  <a class="active" style="width:108px">Home</a>
  <a style="width:115px">About Us</a>
  <a style="width:140px">Accounting</a>
  <a style="width:115px">Careers</a>
  <a style="width:105px">Auditing</a>
  <a style="width:156px">Contacts</a>
</nav>

<div class="abs slider" role="img" aria-label="Photo of two smiling colleagues reviewing a document in an office"></div>
<div class="abs caption">
  <h1>R J Penn Accounting</h1>
  <p>Lorem ipsum dolor sit amet, consectetur adipi-scing elit, sed do eiusmod tempor incididunt ut labore et dolore magna aliqua.</p>
  <div class="dots"><span class="on"></span><span></span><span></span><span></span></div>
</div>

<h2 class="abs section-title welcome-title">Welcome To <em>R J Penn Accounting</em></h2>
<div class="abs welcome-photo" role="img" aria-label="Photo of a smiling businesswoman in an office"></div>
<div class="abs welcome-body">
  <h3>R J Penn Accounting &amp; SMSF Auditing</h3>
  <p>Ean nonumauris hasel lci miumeios penatib magnis dis parntsre neruased abnritatis et quasi tas. Mertyades jertyse fertaseras nertyase.Narnteua eruased penatib magnis dis abnritatis et quasi kertas. Ean nonumauris hasel lci miumeios penatib magnis dis parntsre neruased abnritatis et quasi tas.</p>
  <p>Ean nonumauris hasel lci miumeios penatib magnis dis parntsre neruased abnritatis et quasi tas. Mertyades jertyse fertaseras nertyase.Narnteua eruased penatib magnis dis abnritatis</p>
</div>

<h2 class="abs section-title testi-title">Testimonials</h2>
<div class="abs testi-dots"><span></span><span></span><span></span><span class="on"></span></div>
<div class="abs quote">
  <span class="qmark" style="left:12px;top:8px">“</span>
  <p>Lorem ipsum dolor sit amet, consectetur adipiscing elit, sed do eiusmod tempor incididunt ut labore et dolore magna aliqua. Ut enim ad minim veniam, quis nostrud exercitation ullamco laboris nisi ut</p>
  <span class="qmark" style="right:14px;top:112px">”</span>
</div>
<svg class="abs" style="left:858px;top:701px" width="20" height="14" aria-hidden="true"><path d="M0 0H20V14Z" fill="#f5f5f5"/></svg>
<div class="abs quote-author">John Doe</div>

<div class="abs service-photo s1" role="img" aria-label="Photo of business people shaking hands at a meeting"></div>
<div class="abs service-photo s2" role="img" aria-label="Photo of hands reviewing financial charts with a tablet"></div>
<div class="abs service" style="left:147px">
  <h3>Accounting Services</h3>
  <p>Lorem ipsum dolor sit amet, consectetur adipiscing elit, sed do eiusmod tempor incididunt ut labore et dolore magna aliqua. Ut enim ad minim veniam, quis nostrud exercitation ullamco laboris nisi</p>
</div>
<div class="abs service" style="left:400px">
  <h3>SMSF Auditing</h3>
  <p>Lorem ipsum dolor sit amet, consectetur adipiscing elit, sed do eiusmod tempor incididunt ut labore et dolore magna aliqua. Ut enim ad minim veniam, quis nostrud exercitation ullamco laboris nisi</p>
</div>

<div class="abs news-head">News &amp; Events<span class="news-arrows"><span>‹</span><span>›</span></span></div>
<article class="abs news-item n1">
  <div class="thumb" role="img" aria-label="Photo of a businessman signing papers"></div>
  <div><h4>Sed ut perspiciatis unde omnis iste natus</h4><p>Lorem ipsum dolor sit amet, consectetur adipiscing elit, sed do eiusmod tempor</p></div>
</article>
<div class="abs news-sep"></div>
<article class="abs news-item n2">
  <div class="thumb" role="img" aria-label="Photo of colleagues talking at a desk"></div>
  <div><h4>Sed ut perspiciatis unde omnis iste natus</h4><p>Lorem ipsum dolor sit amet, consectetur adipiscing elit, sed do eiusmod tempor</p></div>
</article>

<footer class="abs footer"></footer>
<div class="abs fcol" style="left:171px"><h4>About Us</h4><ul><li>Company Info</li><li>Clients</li><li>Partners</li></ul></div>
<div class="abs fcol" style="left:294px"><h4>Join In</h4><ul><li>Sign Up</li><li>Forums</li><li>Promotions</li></ul></div>
<div class="abs fcol" style="left:412px"><h4>Advice</h4><ul><li>FAQ</li><li>Accounting</li><li>Services</li></ul></div>

<svg class="abs call-icons" width="64" height="34" aria-hidden="true">
  <circle cx="17" cy="17" r="17" fill="#c8102e"/>
  <rect x="10" y="10" width="14" height="14" rx="3" fill="none" stroke="#fff" stroke-width="2"/>
  <path d="M14 13v8h6" stroke="#fff" stroke-width="2" fill="none"/>
  <circle cx="46" cy="17" r="17" fill="#555" stroke="#fff" stroke-width="2"/>
  <rect x="37" y="11" width="18" height="12" fill="none" stroke="#fff" stroke-width="1.5"/>
  <path d="M37 11l9 7 9-7" stroke="#fff" stroke-width="1.5" fill="none"/>
</svg>
<div class="abs call">
  <div class="label">CALL US NOW!</div>
  <div class="phone">+0400 555 218</div>
  <div class="mail">office@pennsmsf.net.au</div>
</div>

<div class="abs badge" role="img" aria-label="Member badge"></div>
<div class="abs copy">© 2012 | PRIVACY POLICY</div>
<div class="abs foot-social" aria-label="Social links">
  <span style="background:#3b5b9a"></span><span style="background:#2a9fd6"></span><span style="background:#f07a1a"></span><span style="background:#c8102e"></span>
</div>

</body>
</html>
```